Wordpress Website Design/Launch for Aerial Drone Company

My company (Skyward Lens Reels) recently obtained NAB 333 clearance to fly drones for commercial use. I am a needing a very simple, but very visual & techy (icons/colors) look and feel website. aerial images of cities, solar farms, agriculture, buildings can be used since our services will focus on providing aerial video & photography for the following sectors:

- Real Estate Videos for commercial, industrial, retail, multi-family and residential, big focus on developers (new construction type projects. (main market)

- Agricultural videos

- Utilities (electrical line inspection, hydro dams, pipelines, sewage plants, solar farms, fracking operations.

- Hospitality (hotels, resorts)

- Retirement Communities

- Hospitals

- CONSERVATION, ENVIRONMENTAL REGULATION AND COMPLIANCE

- Disaster Relief

- Sporting Events / Festivals / Stadiums, Ballparks
- International availability

This It needs to be WordPress
Easily managed by my team on the backend (including: adding copy, uploading and changing videos and pictures)
Must have a blog
No social media now but needs to have plugins added so we can link when ready

The site should appeal to and have a call to action on every page: contact us via phone, contact form, and click the videos (will need to add) .

Right now I see only 5 pages:
Home (background flying videos through cities/over buildings on streets etc ??)
About Us
Services (see above service areas will need icons for each)
Our Work
Contact Us (needs to integrate into TelvoCRM)
Blog

I am looking for the website to be designed, coded and launch on our hosting server (hostmerlo).

Example of a website
http://www.glidingotterstudios.example

** We do not have a logo so I would like to see whys you can be creative with our name. The website domain is www.skywardlensreels.example.

Target Market(s)

Target market will be:

Real Estate Market (Residential, Commercial, Industrial, developers)
Utilities (Oil companies, electric companies, natural gas companies)
Hospitals
Hotels & Resorts
Farmers (agricultural survey)
Cities & Municipals for aerial surveying/builiding inspections
Blue Harbor / Disaster Relief
Sporting Events / Stadiums - football/Baseball / High School sports

Industry/Entity Type

It Company

Number of Pages Required

5+ page

Requirements
Must have
• Must be very visual
• Include custom icons for the target audience / services
• background video on the home page/ additional pages of flying through cities/streets/ by buildings/ over land / solar farms etc.
• Clean professional look / simple
Nice to have
• I am open to all ideas
• unique logo for our name "Skyward Lens Reels"

```html
<!DOCTYPE html>
<html lang="en">
<head>
<meta charset="utf-8">
<title>Skyward Lens Reels</title>
<link href="https://fonts.googleapis.com/css2?family=Quicksand:wght@500;700&family=Open+Sans:wght@400;600;700&display=swap" rel="stylesheet">
<style>
:root{
  --blue:#2aa7df;
  --blue-dark:#1d8fc4;
  --ink:#2b2f33;
  --text:#6b7075;
  --dark:#33383c;
  --darker:#2a2e31;
  --line:#e3e6e8;
  --foot:#f3f4f5;
  --white:#ffffff;
}
*{box-sizing:border-box;margin:0;padding:0}
html,body{width:1200px;height:2668px;overflow:hidden}
body{font-family:"Open Sans",Arial,sans-serif;color:var(--text);background:var(--white);font-size:13px;line-height:1.6}
h1,h2,h3{font-family:"Quicksand","Open Sans",sans-serif;color:var(--ink)}

/* hero */
.hero{position:relative;height:640px;background:linear-gradient(180deg,#7fa6c2 0%,#9bb3c2 30%,#6f8589 55%,#3e6c86 75%,#2f6f8f 100%)}
.topbar{position:absolute;top:0;left:0;right:0;height:70px;display:flex;align-items:center;padding:0 72px}
.brand{display:flex;align-items:center;gap:10px;font-family:"Quicksand",sans-serif;font-weight:700;font-size:20px;color:var(--white);letter-spacing:1px;text-transform:uppercase;line-height:1}
.brand-mark{width:14px;height:14px;background:var(--white)}
.nav{display:flex;gap:30px;margin-left:auto;margin-right:50px}
.nav a{color:var(--white);text-decoration:none;font-size:12px;font-weight:600;letter-spacing:.5px;padding-bottom:4px}
.nav a.active{border-bottom:2px solid var(--white)}
.cta-videos{display:flex;align-items:center;gap:10px;background:var(--blue);color:var(--white);font-size:12px;font-weight:700;text-transform:uppercase;padding:10px 18px;line-height:1.1}
.hero-copy{position:absolute;top:280px;left:0;right:0;text-align:center;color:var(--white)}
.hero-copy .welcome{font-family:"Quicksand",sans-serif;font-weight:700;font-size:30px}
.hero-copy h1{color:var(--white);font-size:62px;font-weight:700;line-height:1.1;margin:4px 0 12px}
.hero-copy p{font-size:15px;line-height:1.5}
.arrow{position:absolute;top:340px;width:44px;height:44px;border-radius:50%;background:rgba(255,255,255,.85);display:flex;align-items:center;justify-content:center}
.arrow.prev{left:72px}.arrow.next{right:72px}

/* services */
.services{height:490px;padding-top:60px;text-align:center}
.section-title{font-size:32px;font-weight:700}
.title-rule{width:60px;height:3px;background:var(--blue);margin:12px auto 0}
.service-grid{width:900px;margin:40px auto 0;display:grid;grid-template-columns:repeat(5,180px)}
.service{height:140px;display:flex;flex-direction:column;align-items:center;justify-content:center;gap:12px;border-right:1px solid var(--line);border-bottom:1px solid var(--line)}
.service:nth-child(5n){border-right:none}
.service:nth-child(n+6){border-bottom:none}
.service span{font-size:13px;color:var(--ink);font-weight:600;line-height:1.3}

/* videos */
.work{height:495px;background:var(--dark);padding:35px 72px 0}
.work-grid{display:grid;grid-template-columns:repeat(3,336px);gap:24px}
.video-thumb{height:200px;position:relative}
.video-bar{position:absolute;left:0;right:0;bottom:0;height:28px;background:rgba(0,0,0,.55);display:flex;align-items:center;gap:10px;padding:0 10px}
.video-bar .track{flex:1;height:3px;background:rgba(255,255,255,.4)}
.video-bar .track i{display:block;width:30%;height:100%;background:var(--blue)}
.thumb-a{background:linear-gradient(135deg,#6f8c6a,#9aa7a2 50%,#55625b)}
.thumb-b{background:linear-gradient(135deg,#62845a,#8ea57a 50%,#6b7d6e)}
.thumb-c{background:linear-gradient(135deg,#8fa3a8,#c8d0d0 50%,#5f7a6a)}
.work h3{color:var(--white);font-family:"Open Sans",sans-serif;font-weight:600;font-size:18px;margin:22px 0 8px}
.work p{color:#b7bcc0;font-size:12px}
.btn{display:inline-block;background:var(--blue);color:var(--white);font-size:12px;font-weight:700;text-transform:uppercase;padding:12px 26px;line-height:1}
.work .btn-row{text-align:center;margin-top:40px}

/* blog */
.blog{height:560px;padding:30px 72px 0}
.blog h2{font-size:32px;font-weight:700;margin-bottom:28px}
.blog-grid{display:grid;grid-template-columns:repeat(3,336px);gap:24px}
.blog-img{height:210px}
.img-a{background:linear-gradient(160deg,#7d98a8,#a4b3a6 60%,#5f7760)}
.img-b{background:linear-gradient(160deg,#8a9a86,#b6b9a2 50%,#67735b)}
.img-c{background:linear-gradient(160deg,#6f8a5c,#9cab7e 50%,#5b6f56)}
.blog h3{font-family:"Open Sans",sans-serif;font-size:16px;font-weight:700;margin-top:18px}
.blog .date{font-size:11px;color:#9aa0a4;margin:2px 0 8px}
.blog p{font-size:12px}
.read-more{display:inline-block;margin-top:14px;color:var(--blue);font-size:11px;font-weight:700;text-transform:uppercase}

/* newsletter */
.newsletter{height:72px;background:var(--darker);display:flex;align-items:center;padding:0 72px;gap:18px}
.newsletter h3{color:var(--white);font-family:"Open Sans",sans-serif;font-size:18px;font-weight:600;margin-right:auto}
.field{height:34px;background:var(--white);color:#9aa0a4;font-size:12px;padding:0 12px;display:flex;align-items:center}
.newsletter .field{width:230px}
.newsletter .btn{padding:11px 22px}

/* footer */
.footer{height:356px;background:var(--foot);padding:30px 72px 0;position:relative}
.footer-grid{display:grid;grid-template-columns:250px 270px 1fr;gap:20px}
.footer h4{font-family:"Open Sans",sans-serif;color:var(--ink);font-size:14px;font-weight:700;margin-bottom:14px}
.links a{display:block;color:var(--text);text-decoration:none;font-size:12px;line-height:2.1}
.contact-line{display:flex;gap:12px;align-items:flex-start;margin-bottom:14px;font-size:12px;line-height:1.5}
.contact-line .ic{width:30px;height:30px;border-radius:50%;background:var(--blue);display:flex;align-items:center;justify-content:center;flex:none}
.form-note{font-size:12px;margin-bottom:10px}
.form-grid{display:grid;grid-template-columns:1fr 1fr;gap:10px}
.form-grid .field{border:1px solid var(--line)}
.form-grid .message{grid-column:1/3;height:80px;align-items:flex-start;padding-top:8px}
.form-grid .btn{grid-column:1/3;text-align:center}
.copyright{position:absolute;left:72px;bottom:22px;font-size:11px;line-height:1.6}
</style>
</head>
<body>

<header class="hero">
  <div role="img" aria-label="Aerial photograph of a harbour city skyline with waterfront and bridge" style="position:absolute;inset:0"></div>
  <div class="topbar">
    <div class="brand"><span class="brand-mark"></span>Skyward Lens Reels</div>
    <nav class="nav">
      <a class="active" href="#">HOME</a><a href="#">ABOUT</a><a href="#">SERVICES</a><a href="#">OUR WORK</a><a href="#">BLOG</a><a href="#">CONTACT</a>
    </nav>
    <div class="cta-videos">
      <svg width="22" height="22" viewBox="0 0 22 22"><circle cx="11" cy="11" r="10" fill="none" stroke="#fff" stroke-width="2"/><path d="M9 7l6 4-6 4z" fill="#fff"/></svg>
      <span>Click the<br>Videos</span>
    </div>
  </div>
  <div class="hero-copy">
    <div class="welcome">Welcome to</div>
    <h1>Skyward Lens Reels</h1>
    <p>Lorem ipsum dolor sit amet, consectetur adipiscing elit, sed diam nonummy nibh euismod<br>tincidunt ut laoreet dolore magna aliquam erat volutpat ut wisi enim.</p>
  </div>
  <div class="arrow prev"><svg width="14" height="14" viewBox="0 0 14 14"><path d="M9 2L4 7l5 5" fill="none" stroke="#33383c" stroke-width="2"/></svg></div>
  <div class="arrow next"><svg width="14" height="14" viewBox="0 0 14 14"><path d="M5 2l5 5-5 5" fill="none" stroke="#33383c" stroke-width="2"/></svg></div>
</header>

<section class="services">
  <h2 class="section-title">Advantage Services We Provide</h2>
  <div class="title-rule"></div>
  <div class="service-grid">
    <div class="service">
      <svg width="46" height="46" viewBox="0 0 46 46" fill="#2aa7df"><rect x="4" y="14" width="14" height="30"/><rect x="20" y="4" width="14" height="40"/><rect x="36" y="22" width="8" height="22"/></svg>
      <span>Real Estate</span></div>
    <div class="service">
      <svg width="46" height="46" viewBox="0 0 46 46" fill="#2aa7df"><rect x="6" y="18" width="20" height="12"/><rect x="22" y="10" width="12" height="20"/><circle cx="12" cy="36" r="7"/><circle cx="34" cy="38" r="5"/></svg>
      <span>Agricultural</span></div>
    <div class="service">
      <svg width="46" height="46" viewBox="0 0 46 46" fill="#2aa7df"><path d="M6 8h34l4 20H2z"/><rect x="21" y="28" width="4" height="12"/><rect x="12" y="40" width="22" height="3"/><circle cx="40" cy="6" r="4"/></svg>
      <span>Utilities</span></div>
    <div class="service">
      <svg width="46" height="46" viewBox="0 0 46 46" fill="#2aa7df"><path d="M4 20a19 15 0 0 1 38 0z"/><rect x="22" y="20" width="3" height="22"/><rect x="8" y="40" width="30" height="3"/></svg>
      <span>Hospitality</span></div>
    <div class="service">
      <svg width="46" height="46" viewBox="0 0 46 46" fill="#2aa7df"><path d="M4 14c8-4 30-4 38 0 0 12-8 18-19 18S4 26 4 14z"/><circle cx="15" cy="19" r="3" fill="#fff"/><circle cx="31" cy="19" r="3" fill="#fff"/></svg>
      <span>Festivals</span></div>
    <div class="service">
      <svg width="46" height="46" viewBox="0 0 46 46" fill="#2aa7df"><rect x="4" y="6" width="38" height="5"/><rect x="9" y="14" width="28" height="5"/><rect x="14" y="22" width="20" height="5"/><rect x="18" y="30" width="12" height="5"/><rect x="21" y="38" width="6" height="5"/></svg>
      <span>Disaster<br>Relief</span></div>
    <div class="service">
      <svg width="46" height="46" viewBox="0 0 46 46" fill="#2aa7df"><rect x="6" y="10" width="34" height="32"/><rect x="20" y="16" width="6" height="16" fill="#fff"/><rect x="15" y="21" width="16" height="6" fill="#fff"/></svg>
      <span>Hospitals</span></div>
    <div class="service">
      <svg width="46" height="46" viewBox="0 0 46 46" fill="#2aa7df"><circle cx="15" cy="12" r="6"/><circle cx="31" cy="12" r="6"/><rect x="8" y="20" width="14" height="22" rx="4"/><rect x="24" y="20" width="14" height="22" rx="4"/></svg>
      <span>Retirement<br>Communities</span></div>
    <div class="service">
      <svg width="46" height="46" viewBox="0 0 46 46" fill="#2aa7df"><path d="M6 40C6 20 20 6 40 6c0 20-14 34-34 34z"/><path d="M8 38L30 16" stroke="#fff" stroke-width="2"/></svg>
      <span>Environmental</span></div>
    <div class="service">
      <svg width="46" height="46" viewBox="0 0 46 46" fill="none" stroke="#2aa7df" stroke-width="3"><circle cx="23" cy="23" r="18"/><ellipse cx="23" cy="23" rx="8" ry="18"/><path d="M5 23h36M8 14h30M8 32h30"/></svg>
      <span>International<br>Availability</span></div>
  </div>
</section>

<section class="work">
  <div class="work-grid">
    <article>
      <div class="video-thumb thumb-a" role="img" aria-label="Aerial video still of a residential neighbourhood">
        <div class="video-bar"><svg width="10" height="12" viewBox="0 0 10 12"><path d="M0 0l10 6-10 6z" fill="#fff"/></svg><div class="track"><i></i></div></div>
      </div>
      <h3>Real Estate</h3>
      <p>Lorem ipsum dolor sit amet, consectetuer adipiscing elit, sed diam nonummy nibh euismod tincidunt ut laoreet dolore magna aliquam erat volutpat.</p>
    </article>
    <article>
      <div class="video-thumb thumb-b" role="img" aria-label="Aerial video still of green farmland and fields">
        <div class="video-bar"><svg width="10" height="12" viewBox="0 0 10 12"><path d="M0 0l10 6-10 6z" fill="#fff"/></svg><div class="track"><i></i></div></div>
      </div>
      <h3>Agricultural</h3>
      <p>Lorem ipsum dolor sit amet, consectetuer adipiscing elit, sed diam nonummy nibh euismod tincidunt ut laoreet dolore magna aliquam erat volutpat.</p>
    </article>
    <article>
      <div class="video-thumb thumb-c" role="img" aria-label="Aerial video still of a large solar farm">
        <div class="video-bar"><svg width="10" height="12" viewBox="0 0 10 12"><path d="M0 0l10 6-10 6z" fill="#fff"/></svg><div class="track"><i></i></div></div>
      </div>
      <h3>Utilities</h3>
      <p>Lorem ipsum dolor sit amet, consectetuer adipiscing elit, sed diam nonummy nibh euismod tincidunt ut laoreet dolore magna aliquam erat volutpat.</p>
    </article>
  </div>
  <div class="btn-row"><span class="btn">More Videos</span></div>
</section>

<section class="blog">
  <h2>Latest Blog</h2>
  <div class="blog-grid">
    <article>
      <div class="blog-img img-a" role="img" aria-label="Aerial photo of city towers and a park"></div>
      <h3>Lorem ipsum dolor sit amet</h3>
      <div class="date">12 Jan 2018 | 3 Comments</div>
      <p>Lorem ipsum dolor sit amet, consectetuer adipiscing elit, sed diam nonummy nibh euismod tincidunt ut laoreet dolore magna aliquam erat volutpat.</p>
      <span class="read-more">Read More</span>
    </article>
    <article>
      <div class="blog-img img-b" role="img" aria-label="Aerial photo of a suburban building site"></div>
      <h3>Lorem ipsum dolor sit amet</h3>
      <div class="date">12 Jan 2018 | 3 Comments</div>
      <p>Lorem ipsum dolor sit amet, consectetuer adipiscing elit, sed diam nonummy nibh euismod tincidunt ut laoreet dolore magna aliquam erat volutpat.</p>
      <span class="read-more">Read More</span>
    </article>
    <article>
      <div class="blog-img img-c" role="img" aria-label="Aerial photo of a town beside green hills"></div>
      <h3>Lorem ipsum dolor sit amet</h3>
      <div class="date">12 Jan 2018 | 3 Comments</div>
      <p>Lorem ipsum dolor sit amet, consectetuer adipiscing elit, sed diam nonummy nibh euismod tincidunt ut laoreet dolore magna aliquam erat volutpat.</p>
      <span class="read-more">Read More</span>
    </article>
  </div>
</section>

<section class="newsletter">
  <svg width="34" height="26" viewBox="0 0 34 26"><path d="M0 12L34 0 26 26 16 18z" fill="#fff"/><path d="M16 18L34 0" stroke="#2a2e31" stroke-width="2"/></svg>
  <h3>Subscribe Our Newsletter!</h3>
  <div class="field">Enter Your Name</div>
  <div class="field">Enter Your Email</div>
  <span class="btn">Subscribe</span>
</section>

<footer class="footer">
  <div class="footer-grid">
    <div class="links">
      <h4>Quick Links</h4>
      <a href="#">Home</a><a href="#">About</a><a href="#">Services</a><a href="#">Our Work</a><a href="#">Blog</a><a href="#">Contact</a>
    </div>
    <div>
      <h4>Get in Touch</h4>
      <div class="contact-line"><span class="ic"><svg width="12" height="16" viewBox="0 0 12 16"><path d="M6 0a6 6 0 0 1 6 6c0 4-6 10-6 10S0 10 0 6a6 6 0 0 1 6-6z" fill="#fff"/><circle cx="6" cy="6" r="2" fill="#2aa7df"/></svg></span><span>123, Lorem Ipsum Street,<br>Dolor Sit Amet - 000000</span></div>
      <div class="contact-line"><span class="ic"><svg width="14" height="14" viewBox="0 0 14 14"><path d="M3 0l3 3-2 2c1 2 3 4 5 5l2-2 3 3-2 3C6 14 0 8 0 3z" fill="#fff"/></svg></span><span>Phone:<br>000-000-0000</span></div>
      <div class="contact-line"><span class="ic"><svg width="14" height="10" viewBox="0 0 14 10"><rect width="14" height="10" fill="#fff"/><path d="M0 0l7 6 7-6" fill="none" stroke="#2aa7df" stroke-width="1.5"/></svg></span><span>Email:<br>info@skywardlensreels.example</span></div>
    </div>
    <div>
      <h4>Contact Form</h4>
      <p class="form-note">Fill below details and contact now</p>
      <div class="form-grid">
        <div class="field">Name</div><div class="field">Email</div>
        <div class="field">Phone</div><div class="field">Subject</div>
        <div class="field message">Message</div>
        <span class="btn">Submit</span>
      </div>
    </div>
  </div>
  <div class="copyright">Copyright © 2018 Skyward Lens Reels. All Rights Reserved.<br>Terms &amp; Conditions | Privacy Policy | Terms of Use</div>
</footer>

</body>
</html>
```